Brambleway Gardening Services. A6 flyer single sided

Need an A6 flyer designing. Single sided.
I am a gardener.
I do lawn mowing - one-off garden tidy ups or regular fortnightly visits.
All kinds of trees expertly felled, topped or pruned.
Hedge cutting.
Fencing replaced or repaired.
Fully insured.
Access to fully qualified and licenced tree arborist
07741 206319 or 01632 470918.

I have attached my business card and letter head logo.
I'm open to new designs without incorporating any of my artwork.

Industry/Entity Type

Gardener

```html
<!DOCTYPE html>
<html lang="en">
<head>
<meta charset="utf-8">
<title>Brambleway Garden Services – Flyer</title>
<link rel="stylesheet" href="https://fonts.googleapis.com/css2?family=Montserrat:wght@400;500&family=Quicksand:wght@500;600&family=Questrial&display=swap">
<style>
  :root {
    --forest: #1f5a1b;
    --forest-deep: #184a15;
    --leaf: #5fa12a;
    --lime: #8cc63f;
    --lime-bright: #b5e23a;
    --hedge-dark: #2c6a1c;
    --hedge-mid: #4f9a2c;
    --hedge-light: #86c24a;
    --sleeve: #1e2a44;
    --white: #ffffff;
    --band-text: #1f4d17;
  }
  * { margin: 0; padding: 0; box-sizing: border-box; }
  html, body { width: 846px; height: 1200px; overflow: hidden; background: var(--white); }
  .flyer {
    position: relative;
    width: 846px;
    height: 1200px;
    overflow: hidden;
    background: var(--forest);
    color: var(--white);
  }
  .backdrop { position: absolute; inset: 0; }
  .hero-photo {
    position: absolute;
    left: 0; top: 0;
    width: 846px; height: 580px;
    background:
      radial-gradient(ellipse 300px 150px at 300px 60px, rgba(30,42,68,0.85), rgba(30,42,68,0) 70%),
      radial-gradient(circle 130px at 120px 330px, rgba(134,194,74,0.7), rgba(134,194,74,0) 70%),
      radial-gradient(circle 160px at 700px 220px, rgba(134,194,74,0.6), rgba(134,194,74,0) 70%),
      radial-gradient(circle 140px at 480px 420px, rgba(44,106,28,0.8), rgba(44,106,28,0) 70%),
      radial-gradient(circle 120px at 760px 60px, rgba(160,210,90,0.7), rgba(160,210,90,0) 70%),
      linear-gradient(170deg, var(--hedge-mid) 0%, var(--hedge-dark) 50%, var(--hedge-mid) 100%);
  }
  .grass {
    position: absolute;
    background: linear-gradient(to top, rgba(140,198,63,0.5), rgba(140,198,63,0));
  }
  .grass--left { left: 0; bottom: 200px; width: 230px; height: 300px; border-top-right-radius: 50% 100%; }
  .grass--right { right: 0; bottom: 200px; width: 300px; height: 170px; border-top-left-radius: 70% 100%; }
  .brand-name {
    position: absolute;
    left: 0; right: 0;
    top: 562px;
    text-align: center;
    font-family: "Montserrat", sans-serif;
    font-weight: 400;
    font-size: 64px;
    line-height: 80px;
    letter-spacing: 3px;
    text-transform: uppercase;
    padding-left: 40px;
  }
  .brand-rule {
    position: absolute;
    left: 112px; top: 730px;
    width: 640px; height: 1px;
    background: var(--leaf);
  }
  .services {
    position: absolute;
    left: 238px; top: 742px;
    list-style: none;
    font-family: "Quicksand", sans-serif;
    font-weight: 500;
    font-size: 31px;
  }
  .services li {
    display: flex;
    align-items: center;
    height: 49px;
  }
  .services svg { width: 22px; height: 22px; margin-right: 26px; flex: none; }
  .credential-band {
    position: absolute;
    left: 0; top: 1000px;
    width: 846px; height: 43px;
    background: var(--lime);
    color: var(--band-text);
    font-family: "Quicksand", sans-serif;
    font-weight: 600;
    font-size: 27px;
    letter-spacing: 0.6px;
    line-height: 43px;
    text-align: center;
  }
  .contact {
    position: absolute;
    left: 150px; top: 1062px;
    display: flex;
    align-items: center;
  }
  .contact-icon { width: 60px; height: 60px; margin-right: 62px; }
  .contact-numbers {
    font-family: "Questrial", sans-serif;
    font-size: 52px;
    line-height: 66px;
    letter-spacing: 3px;
  }
</style>
</head>
<body>
<main class="flyer">
  <div class="hero-photo" role="img" aria-label="Photo of gloved hands trimming a green hedge with red-handled secateurs"></div>

  <svg class="backdrop" viewBox="0 0 846 1200" width="846" height="1200" aria-hidden="true">
    <path d="M0 528 C 230 515 420 370 610 352 C 720 344 800 372 846 405 L846 1200 L0 1200 Z" fill="var(--lime)"/>
    <path d="M0 545 C 240 535 440 395 615 385 C 715 380 790 440 846 520 L846 1200 L0 1200 Z" fill="var(--leaf)"/>
    <path d="M0 560 C 250 552 450 420 625 425 C 720 428 795 540 846 640 L846 1200 L0 1200 Z" fill="var(--forest)"/>
  </svg>

  <div class="grass grass--left" role="img" aria-label="Illustrated grass tufts with small daisies"></div>
  <div class="grass grass--right" role="img" aria-label="Illustrated grass tufts with small daisies"></div>

  <h1 class="brand-name">Brambleway<br>Garden Services</h1>
  <div class="brand-rule"></div>

  <ul class="services">
    <li><svg viewBox="0 0 24 24"><path d="M12 2l2.9 6.3 6.9.7-5.2 4.6 1.5 6.8L12 16.9 5.9 20.4l1.5-6.8L2.2 9l6.9-.7z" fill="var(--lime)"/></svg>Lawn mowing &amp; garden tidy ups</li>
    <li><svg viewBox="0 0 24 24"><path d="M12 2l2.9 6.3 6.9.7-5.2 4.6 1.5 6.8L12 16.9 5.9 20.4l1.5-6.8L2.2 9l6.9-.7z" fill="var(--lime)"/></svg>Trees felled, topped or pruned</li>
    <li><svg viewBox="0 0 24 24"><path d="M12 2l2.9 6.3 6.9.7-5.2 4.6 1.5 6.8L12 16.9 5.9 20.4l1.5-6.8L2.2 9l6.9-.7z" fill="var(--lime)"/></svg>Hedge cutting</li>
    <li><svg viewBox="0 0 24 24"><path d="M12 2l2.9 6.3 6.9.7-5.2 4.6 1.5 6.8L12 16.9 5.9 20.4l1.5-6.8L2.2 9l6.9-.7z" fill="var(--lime)"/></svg>Fencing replaced or repaired</li>
    <li><svg viewBox="0 0 24 24"><path d="M12 2l2.9 6.3 6.9.7-5.2 4.6 1.5 6.8L12 16.9 5.9 20.4l1.5-6.8L2.2 9l6.9-.7z" fill="var(--lime)"/></svg>Fully insured</li>
  </ul>

  <p class="credential-band">Access to fully qualified and licenced tree arborist</p>

  <div class="contact">
    <svg class="contact-icon" viewBox="0 0 60 60" aria-hidden="true">
      <circle cx="30" cy="30" r="29" fill="var(--lime-bright)"/>
      <circle cx="30" cy="30" r="21" fill="var(--white)"/>
      <path d="M23 18c1.5-1 3-.5 3.7.8l2 3.8c.6 1.2.2 2.4-.8 3.1l-1.4 1c.8 2.6 3 5 5.6 6.1l1.1-1.3c.8-1 2.1-1.2 3.2-.5l3.5 2.2c1.2.8 1.5 2.3.5 3.7l-1.3 1.7c-1 1.3-2.8 1.8-4.4 1.2-7-2.6-12-8-14-14.8-.5-1.6 0-3.3 1.3-4.3z" fill="var(--leaf)"/>
    </svg>
    <div class="contact-numbers">
      <div>07741 206319</div>
      <div>01632 470918</div>
    </div>
  </div>
</main>
</body>
</html>
```